Safety Training company business card design

We are after a high quality, professional business card. We are open to a single or double sided card.

The winning designer must provide the card in a format where we can easily change the name and details of the different people in our organization.

Brindle Guard's company colour is lime green.

We provide all aspects of safety advisory and training for the Building, Civil Construction, Mining, Oil and Gas, Manufacturing, Rail, Rural and Retail sectors.

Visit our website www.brindleguard-example.com.au for training competencies we offer along with our other services including RPL's, safety audits, professional development and client support.

Target Market(s)

Those in the Building, Civil Construction, Mining, Oil and Gas, Manufacturing, Rail, Rural and Retail industries.

Industry/Entity Type

Training

Contact Information for Business Card

Brindle Guard
Safety and Training
Thomas Wellacott
Director
M 0400 555 217
thomas@brindleguard-example.com.au
www.brindleguard-example.com.au
(2 business addresses:)
Penhollow High Risk Training Centre
18 Juniper Parade, Penhollow Q 4000 P 3900 5512 F 3900 5519
Ellerwick Training Centre
67 Talbot Lane, Ellerwick Q 4000 P 4900 2641 F 4900 2648

Colors
9bcb3c

Requirements
Must have
• Lime green must be the main colour. must include BG logo attached, and state Brindle Guard (Safety and Training in smaller/different font).

State something along the lines of:

Nice to have
• We offer remote training and we can come to you.

```html
<!DOCTYPE html>
<html lang="en">
<head>
<meta charset="utf-8">
<title>Brindle Guard – Business Card</title>
<link rel="stylesheet" href="https://fonts.googleapis.com/css2?family=Mulish:ital,wght@0,300;0,400;0,700;0,800;1,700&display=swap">
<style>
  :root {
    --lime: #9bcb3c;
    --lime-icon: #8fc43c;
    --yellow: #ffe600;
    --sky: #87b0d8;
    --charcoal: #3d4145;
    --charcoal-dark: #2c2f33;
    --ink: #2b2b2b;
    --white: #ffffff;
    --brand-red: #d22a1e;
    --page: #eceeee;
  }
  * { margin: 0; padding: 0; box-sizing: border-box; }
  html, body { width: 1100px; height: 1200px; overflow: hidden; }
  body { background: var(--page); font-family: "Mulish", sans-serif; position: relative; }

  .card {
    position: absolute; left: 119px; width: 829px;
    overflow: hidden; box-shadow: 0 6px 18px rgba(0,0,0,.18);
    background: var(--charcoal);
  }
  .card--front { top: 77px; height: 491px; }
  .card--back { top: 623px; height: 492px; }

  .photo { position: absolute; left: 0; top: 0; width: 100%; }
  .card--front .photo {
    height: 473px;
    background:
      linear-gradient(90deg, rgba(255,215,0,.95) 0%, rgba(240,200,20,.9) 22%, rgba(70,110,160,.85) 40%, rgba(61,65,69,0) 62%),
      linear-gradient(180deg, #4b5056, #3a3e42 60%, #2f3236);
  }
  .card--back .photo {
    height: 474px;
    background: linear-gradient(180deg, #44484d, #35393d 70%, #2e3135);
  }
  .sky-band { position: absolute; top: 0; right: 0; background: var(--sky); }
  .card--front .sky-band { left: 320px; height: 58px; }
  .card--back .sky-band { left: 320px; height: 57px; }
  .denim-strip { position: absolute; top: 0; left: 0; width: 320px; background: linear-gradient(90deg, #2f5f93, #5a86b8 60%, var(--sky)); }
  .card--back .denim-strip { height: 57px; }

  .lime-band { position: absolute; left: 0; width: 100%; background: var(--lime); }
  .card--front .lime-band { top: 58px; height: 125px; }
  .card--back .lime-band { top: 57px; height: 162px; }

  .helmet-area {
    position: absolute; left: 0; top: 183px; width: 440px; height: 290px;
    background: radial-gradient(ellipse at 30% 55%, #ffe11a 0%, #f5c800 45%, rgba(90,120,160,.7) 80%, rgba(61,65,69,0) 100%);
  }

  .brand { position: absolute; left: 180px; top: 80px; display: flex; align-items: center; gap: 14px; }
  .brand__dot { width: 26px; height: 26px; border-radius: 50%; background: var(--brand-red); }
  .brand__name { font-weight: 800; font-size: 48px; letter-spacing: 1px; color: var(--brand-red); line-height: 1; text-transform: uppercase; white-space: nowrap; }
  .brand__tagline {
    position: absolute; left: 344px; top: 136px;
    font-size: 17px; letter-spacing: 8.2px; color: var(--white); font-weight: 400; white-space: nowrap;
  }

  .person { position: absolute; left: 494px; top: 208px; color: var(--white); white-space: nowrap; }
  .person__name { font-weight: 700; font-size: 22px; }
  .person__role { font-weight: 400; font-size: 22px; margin-top: 8px; }

  .contact-list {
    position: absolute; left: 470px; top: 301px; list-style: none;
    color: var(--white); font-size: 18px; font-weight: 300; letter-spacing: -0.2px;
  }
  .contact-list li { display: flex; align-items: center; height: 36px; white-space: nowrap; }
  .contact-list svg { width: 24px; height: 24px; margin-right: 10px; flex: none; }

  .foot-stripe { position: absolute; left: 0; bottom: 0; width: 100%; height: 18px; }

  .sectors {
    position: absolute; left: 0; top: 84px; width: 100%; text-align: center;
    font-style: italic; font-weight: 700; font-size: 21.5px; line-height: 40px; color: var(--ink);
  }

  .centre { position: absolute; top: 258px; color: var(--white); white-space: nowrap; }
  .centre--west { left: 55px; }
  .centre--east { right: 59px; text-align: right; }
  .centre__title { font-weight: 700; font-size: 21px; }
  .centre__address { font-weight: 300; font-size: 21.5px; line-height: 26px; margin-top: 36px; }
  .centre--east .centre__address { margin-top: 38px; }
  .centre__lines { list-style: none; font-weight: 300; font-size: 22px; margin-top: 26px; }
  .centre__lines li { display: flex; align-items: center; height: 28px; gap: 10px; }
  .centre--east .centre__lines li { justify-content: flex-end; }
  .centre__lines svg { width: 22px; height: 22px; flex: none; }
</style>
</head>
<body>

<section class="card card--front" aria-label="Business card front">
  <div class="photo" role="img" aria-label="Photo of a yellow hard hat, denim shirt sleeve and rolled plans on a blurred construction site"></div>
  <div class="sky-band"></div>
  <div class="lime-band"></div>
  <div class="helmet-area" role="img" aria-label="Yellow safety hard hat held under a denim sleeve"></div>

  <div class="brand">
    <span class="brand__dot"></span>
    <span class="brand__name">Brindle Guard</span>
  </div>
  <div class="brand__tagline">SAFETY AND TRAINING</div>

  <div class="person">
    <p class="person__name">Thomas Wellacott</p>
    <p class="person__role">Director</p>
  </div>

  <ul class="contact-list">
    <li>
      <svg viewBox="0 0 26 26" fill="none" stroke="var(--lime-icon)" stroke-width="2"><rect x="7" y="2" width="12" height="21" rx="2"/><line x1="11" y1="19" x2="15" y2="19"/></svg>
      0400 555 217
    </li>
    <li>
      <svg viewBox="0 0 26 26" fill="none" stroke="var(--lime-icon)" stroke-width="2"><rect x="2" y="6" width="22" height="14"/><polyline points="2,6 13,15 24,6"/></svg>
      thomas@brindleguard-example.com.au
    </li>
    <li>
      <svg viewBox="0 0 26 26" fill="none" stroke="var(--lime-icon)" stroke-width="1.6"><circle cx="13" cy="13" r="11"/><ellipse cx="13" cy="13" rx="5" ry="11"/><line x1="2" y1="13" x2="24" y2="13"/><path d="M4 7h18M4 19h18"/></svg>
      www.brindleguard-example.com.au
    </li>
  </ul>

  <svg class="foot-stripe" viewBox="0 0 829 18" preserveAspectRatio="none">
    <rect width="829" height="18" fill="var(--yellow)"/>
    <polygon points="0,0 440,0 360,18 0,18" fill="var(--lime)"/>
  </svg>
</section>

<section class="card card--back" aria-label="Business card back">
  <div class="photo" role="img" aria-label="Blurred construction site scaffolding in dark grey tones"></div>
  <div class="denim-strip" role="img" aria-label="Denim shirt fabric"></div>
  <div class="sky-band"></div>
  <div class="lime-band"></div>

  <p class="sectors">
    We provide all aspects of safety advisory and training<br>
    for Building, Civil Construction, Mining, Oil and Gas,<br>
    Manufacturing, Rail, Rural and Retail sectors
  </p>

  <div class="centre centre--west">
    <p class="centre__title">Penhollow High Risk Training Centre</p>
    <p class="centre__address">18 Juniper Parade,<br>Penhollow Q 4000</p>
    <ul class="centre__lines">
      <li>
        <svg viewBox="0 0 22 22" fill="var(--lime-icon)"><path d="M5 2l4 4-2 3c1 2 3 4 5 5l3-2 4 4-3 3C9 19 3 13 2 5z"/></svg>
        07 3900 5512
      </li>
      <li>
        <svg viewBox="0 0 22 22" fill="none" stroke="var(--lime-icon)" stroke-width="1.8"><rect x="2" y="9" width="18" height="10" rx="1"/><rect x="6" y="3" width="10" height="6"/><line x1="6" y1="14" x2="16" y2="14"/></svg>
        07 3900 5519
      </li>
    </ul>
  </div>

  <div class="centre centre--east">
    <p class="centre__title">Ellerwick Training Centre</p>
    <p class="centre__address">67 Talbot Lane,<br>Ellerwick Q 4000</p>
    <ul class="centre__lines">
      <li>
        <svg viewBox="0 0 22 22" fill="var(--lime-icon)"><path d="M5 2l4 4-2 3c1 2 3 4 5 5l3-2 4 4-3 3C9 19 3 13 2 5z"/></svg>
        07 4900 2641
      </li>
      <li>
        <svg viewBox="0 0 22 22" fill="none" stroke="var(--lime-icon)" stroke-width="1.8"><rect x="2" y="9" width="18" height="10" rx="1"/><rect x="6" y="3" width="10" height="6"/><line x1="6" y1="14" x2="16" y2="14"/></svg>
        07 4900 2648
      </li>
    </ul>
  </div>

  <svg class="foot-stripe" viewBox="0 0 829 18" preserveAspectRatio="none">
    <rect width="829" height="18" fill="var(--lime)"/>
    <polygon points="0,0 420,0 470,18 0,18" fill="var(--yellow)"/>
  </svg>
</section>

</body>
</html>
```